Business Card Design

We need a basic, but modern design card. Our business is a local Queanbeyan/Canberra courier service, but can organise interstate delivery if needed. Our fleet ranges from 1 tonne vans to 8 tonne trucks.

Industry/Entity Type

Business

Contact Information for Business Card

Harbourline Freight
14 Wren Parade
Tarrowvale 2791

Dean Fairley
CEO

Phone: 02 61847315
Fax: 02 61847358
email: dean@harbourlinefreight.example.au

```html
<!DOCTYPE html>
<html lang="en">
<head>
<meta charset="utf-8">
<title>Harbourline Freight – Business Card</title>
<link rel="stylesheet" href="https://fonts.googleapis.com/css2?family=Mulish:wght@400;700;900&display=swap">
<style>
  :root {
    --brand-blue: #0b4f9c;
    --accent-orange: #e8581e;
    --ink: #3a3a3a;
    --divider: #9a9a9a;
    --paper: #ffffff;
  }
  * { margin: 0; padding: 0; box-sizing: border-box; }
  html, body { width: 1200px; height: 759px; overflow: hidden; background: var(--paper); }
  .card {
    position: relative;
    width: 1200px;
    height: 759px;
    background: var(--paper);
    font-family: "Mulish", Arial, sans-serif;
    color: var(--ink);
  }
  .brand-name {
    position: absolute;
    left: 100px;
    top: 84px;
    width: 588px;
    text-align: right;
    font-weight: 900;
    font-size: 70px;
    line-height: 80px;
    text-transform: uppercase;
    color: var(--brand-blue);
    letter-spacing: 1px;
  }
  .divider {
    position: absolute;
    left: 706px;
    top: 78px;
    width: 4px;
    height: 496px;
    background: var(--divider);
  }
  .tagline {
    position: absolute;
    left: 738px;
    top: 140px;
    font-size: 58px;
    font-weight: 400;
    color: var(--brand-blue);
  }
  .contact-list {
    position: absolute;
    right: 531px;
    top: 364px;
    list-style: none;
  }
  .contact-list li {
    display: flex;
    align-items: center;
    justify-content: flex-end;
    height: 55px;
    font-size: 32px;
    font-weight: 400;
    white-space: nowrap;
  }
  .contact-list svg {
    width: 30px;
    height: 30px;
    margin-left: 18px;
    fill: none;
    stroke: var(--accent-orange);
    stroke-width: 2.4;
    stroke-linejoin: round;
    stroke-linecap: round;
  }
  .person {
    position: absolute;
    left: 745px;
    top: 400px;
  }
  .person-name {
    font-size: 38px;
    font-weight: 700;
    color: var(--brand-blue);
    line-height: 50px;
  }
  .person-role {
    font-size: 38px;
    font-weight: 400;
    line-height: 50px;
  }
  .web-band {
    position: absolute;
    left: 0;
    bottom: 0;
    width: 1200px;
    height: 131px;
    background: var(--brand-blue);
  }
  .web-address {
    position: absolute;
    left: 0;
    width: 1274px;
    top: 19px;
    line-height: 50px;
    text-align: center;
    font-size: 40px;
    font-weight: 700;
    color: var(--paper);
    white-space: nowrap;
  }
</style>
</head>
<body>
<div class="card">
  <div class="brand-name">Harbourline<br>Freight</div>
  <div class="divider"></div>
  <div class="tagline">We Deliver</div>

  <ul class="contact-list">
    <li>02 61847315
      <svg viewBox="0 0 24 24" aria-hidden="true"><path d="M6 3l3 1 1 4-2 2c1 2.5 3 4.5 5.5 5.5l2-2 4 1 1 3-2 3C10 20 4 14 3.5 5z"/></svg>
    </li>
    <li>02 61847358
      <svg viewBox="0 0 24 24" aria-hidden="true"><rect x="6" y="3" width="12" height="6"/><rect x="3" y="9" width="18" height="8"/><rect x="7" y="14" width="10" height="7"/><path d="M9 17h6M9 19h6"/></svg>
    </li>
    <li>dean@harbourlinefreight.example.au
      <svg viewBox="0 0 24 24" aria-hidden="true"><rect x="3" y="6" width="18" height="12"/><path d="M3 6l9 7 9-7M3 18l7-6M21 18l-7-6"/></svg>
    </li>
    <li>14 Wren Parade Tarrowvale 2791
      <svg viewBox="0 0 24 24" aria-hidden="true"><path d="M2 11L12 4l10 7"/><rect x="5" y="11" width="14" height="9"/><rect x="10" y="14" width="4" height="6"/></svg>
    </li>
  </ul>

  <div class="person">
    <div class="person-name">Dean Fairley</div>
    <div class="person-role">CEO</div>
  </div>

  <div class="web-band">
    <div class="web-address">www.harbourlinefreight.example.au</div>
  </div>
</div>
</body>
</html>
```